Health and Wellness. I am an energetic, but not over the top, Certified Personal Trainer and Nutriti

I need a flyer, 8.5 x 11, representing my company to be displayed in a Doctor's office that specializes in Pain Medicine. Most, if not all, of these clients experience pain or have some chronic diseases such as high blood pressure, high cholesterol, back pain, joint pain, etc. So the flyer should convey that exercise and nutrition reduce/relieves pain and references some of these ailments. Ideally, the flyer should depict an overweight person exercising with a content, or somewhat content or smiling expression on their face in some part of the flyer. My services cover nutrition and include personal training to where I Ideally train people in their home, equipment permitting, or outside in our local Floridian Parks, and sometimes beaches. This flyer will be in a display case, and the bottom right 8.5 x5 cm will need to be blank, or allow for me to input the back of my business car into it, as I'll have business cards readily available in front of the flyer to be taken. I've included some versions of my logos to be added to the flyer. The other picture is of the flyer holder, with business card area, that this flyer will be presented in. Finally, I've attached a pic of what the back of my business card looks like to be input into that bottom right hand corner. You'll be able to see the area in the bottom right that will display my business cards.
Target Market(s)
People looking for weight loss through Nutrition and Fitness. Those looking to relieve joint and/or back pain or those with Chronic diseases such as high blood pressure, high cholesterol, etc.
Industry/Entity Type
Doctor
Requirements
Must have
- Resemble my Logo's color scheme: Red, Teal, and Grey. Some type of photo of an overweight or slightly overweight person exercising.

```html
<!DOCTYPE html>
<html lang="en">
<head>
<meta charset="utf-8">
<title>Halversen's Fitness – Flyer</title>
<link rel="stylesheet" href="https://fonts.googleapis.com/css2?family=Montserrat:wght@700;800&family=Roboto+Condensed:wght@400;700&display=swap">
<style>
  :root {
    --red: #e0262f;
    --red-deep: #b81820;
    --teal: #1a9a8a;
    --charcoal: #2a2b2d;
    --grey-light: #e3e6e6;
    --grey-mid: #c9cfcf;
    --ink: #2f3335;
    --white: #ffffff;
    --stage: #d9dcdc;
  }
  * { margin: 0; padding: 0; box-sizing: border-box; }
  html, body { width: 1200px; height: 1110px; overflow: hidden; }
  body {
    background: var(--stage);
    display: flex; align-items: center; justify-content: center;
    font-family: "Roboto Condensed", sans-serif;
  }
  .flyer {
    position: relative; width: 796px; height: 1030px; overflow: hidden;
    background: linear-gradient(160deg, var(--grey-light), var(--grey-mid));
    box-shadow: 0 6px 24px rgba(0,0,0,.18);
  }
  .flyer-shapes { position: absolute; inset: 0; }
  .hero-photo {
    position: absolute; left: 40px; top: 0; width: 360px; height: 600px;
    background: radial-gradient(ellipse at 45% 40%, rgba(255,120,120,.55), rgba(184,24,32,0) 70%);
    clip-path: polygon(0 0, 100% 0, 70% 100%, 0 100%);
  }
  .brand {
    position: absolute; left: 60px; top: 70px;
    display: flex; align-items: center; gap: 16px;
    font-family: "Montserrat", sans-serif; font-weight: 800;
    color: var(--white); font-size: 26px; letter-spacing: 1px;
  }
  .brand-dot { width: 22px; height: 22px; border-radius: 50%; background: var(--white); }
  .title { position: absolute; left: 56px; top: 190px; color: var(--white); font-family: "Montserrat", sans-serif; font-weight: 800; line-height: .95; }
  .title-name { font-size: 58px; letter-spacing: 2px; }
  .title-word { font-size: 118px; letter-spacing: 3px; }
  .service-tag {
    position: absolute; left: 395px; top: 395px; width: 375px; height: 58px;
    background: var(--teal); color: var(--white);
    font-weight: 700; font-size: 34px; display: flex; align-items: center; justify-content: center;
    letter-spacing: .5px;
  }
  .service-text {
    position: absolute; left: 410px; top: 470px; width: 360px;
    color: var(--ink); font-size: 25px; line-height: 1.15; text-transform: uppercase;
  }
  .training-photo {
    position: absolute; left: 345px; top: 590px; width: 451px; height: 215px;
    background: linear-gradient(120deg, #3a3f44, #6e7478 45%, #a9a59a 80%, #4a4f52);
  }
  .call-bar {
    position: absolute; left: 330px; top: 815px; width: 440px; height: 62px;
    background: var(--teal); color: var(--white);
    font-weight: 700; font-size: 40px; display: flex; align-items: center; justify-content: center; gap: 18px;
  }
  .contacts {
    position: absolute; left: 0; right: 0; top: 905px;
    text-align: center; color: var(--ink); font-weight: 700; font-size: 22px; line-height: 1.5; letter-spacing: .5px;
  }
  .experience-tag {
    position: absolute; left: 0; top: 565px; width: 270px; height: 56px;
    background: #111; color: var(--white);
    font-weight: 700; font-size: 28px; display: flex; align-items: center; padding-left: 26px;
    clip-path: polygon(0 0, 100% 0, 90% 100%, 0 100%);
  }
  .ailments { position: absolute; left: 30px; top: 645px; list-style: none; color: var(--white); font-weight: 700; font-size: 26px; line-height: 1.35; text-transform: uppercase; }
  .ailments li { display: flex; align-items: flex-start; gap: 12px; }
  .ailments svg { flex: none; margin-top: 6px; }
</style>
</head>
<body>
  <main class="flyer">
    <svg class="flyer-shapes" viewBox="0 0 796 1030" aria-hidden="true">
      <polygon points="0,0 500,0 300,560 360,710 280,890 0,890" fill="var(--red)"/>
      <polygon points="500,0 796,0 796,115 455,125" fill="#f1f2f2"/>
      <polygon points="455,125 796,115 796,350 375,360" fill="var(--charcoal)"/>
      <polyline points="510,0 310,560 372,710 290,890" fill="none" stroke="#ffffff" stroke-width="3"/>
    </svg>

    <div class="hero-photo" role="img" aria-label="Photo of a woman training, tinted red"></div>

    <div class="brand"><span class="brand-dot"></span>HALVERSEN'S</div>

    <h1 class="title">
      <span class="title-name">HALVERSEN'S</span><br>
      <span class="title-word">FITNESS</span>
    </h1>

    <div class="service-tag">FITNESS TRAINING</div>
    <p class="service-text">In yor home, online, parks and beaches, bride, groom, and bridal party</p>

    <div class="training-photo" role="img" aria-label="Photo of a group doing plank exercises in a gym"></div>

    <div class="experience-tag">EXPERIENCE</div>
    <ul class="ailments">
      <li><svg width="18" height="18" viewBox="0 0 18 18"><circle cx="9" cy="9" r="9" fill="#fff"/><path d="M7 5l4 4-4 4" stroke="var(--red)" stroke-width="2.4" fill="none"/></svg><span>Blood<br>Pressure</span></li>
      <li><svg width="18" height="18" viewBox="0 0 18 18"><circle cx="9" cy="9" r="9" fill="#fff"/><path d="M7 5l4 4-4 4" stroke="var(--red)" stroke-width="2.4" fill="none"/></svg><span>High<br>Cholesterol</span></li>
      <li><svg width="18" height="18" viewBox="0 0 18 18"><circle cx="9" cy="9" r="9" fill="#fff"/><path d="M7 5l4 4-4 4" stroke="var(--red)" stroke-width="2.4" fill="none"/></svg><span>Back Pain</span></li>
      <li><svg width="18" height="18" viewBox="0 0 18 18"><circle cx="9" cy="9" r="9" fill="#fff"/><path d="M7 5l4 4-4 4" stroke="var(--red)" stroke-width="2.4" fill="none"/></svg><span>Joint Pain</span></li>
    </ul>

    <div class="call-bar"><span>Call Us:</span><span>555-214-0836</span></div>

    <div class="contacts">
      <p>WWW.HALVERSENFIT.COM | HELLO@HALVERSENFIT.COM</p>
      <p>@HALVERSENFIT</p>
    </div>
  </main>
</body>
</html>
```